Modern Website Design for PollMeridian – CX & Loyalty SaaS Platform

We need a modern, professional, and responsive website design for our B2B SaaS platform, PollMeridian. We help companies collect real-time customer feedback, analyze insights, and improve loyalty — combining a powerful CX platform with expert consulting services. The website should clearly communicate who we are and what we offer within the first impression. It should balance data-driven visuals such as dashboards, analytics, and charts with a human, approachable feel. The design must include at least six key pages: Homepage, Product/Services, About, Blog/Resources, Contact/Demo, and Pricing. It should be conversion-focused with clear calls-to-action that encourage visitors to request a demo or contact us. The site must be fully responsive across desktop, tablet, and mobile. It should support multiple languages, starting with English and Danish. Most importantly, the delivery must be a final WordPress website, ready to go live, not just design files.

Target Market(s)

Our target market is medium-to-large B2B organizations. The primary audience includes CX leaders, executives, and managers in customer success and service who want to measure loyalty, understand customer insights, and improve retention.

Industry/Entity Type

Technology / SaaS / Customer Experience

Coding

Coded - Design and coding required

Number of Pages Required

5+ page

Font styles to use
Sans Serif

Requirements
Must have
• The project must deliver a final WordPress website that is fully responsive across all devices. The design should be clean, modern, and SaaS-inspired, with clear calls-to-action on every page. It must also support English and Danish, with a visible language toggle. The site should include visuals of dashboards and analytics that reflect data-driven insights. It must feature sections for case studies or testimonials to build trust. The copywriting should be SEO-friendly, and the design should include smooth animations or hover effects that add polish without making the website feel heavy.
Should not have
• Cluttered layouts, or generic stock photos such as handshakes

```html
<!DOCTYPE html>
<html lang="en">
<head>
<meta charset="utf-8">
<title>PollMeridian – CX Platform + Experts</title>
<link href="https://fonts.googleapis.com/css2?family=Poppins:wght@400;500;600&display=swap" rel="stylesheet">
<style>
:root{
  --green:#14a878;--green-dark:#0f8f66;--blue:#1f56a8;--navy:#1c2333;
  --text:#1d2230;--muted:#6b7280;--line:#e4e8ee;--mint:#eef8f4;--mint2:#e4f4ee;
  --sky:#eef4fc;--lav:#eceffc;--gray:#f6f7f9;--white:#fff;--star:#f29a38;
}
*{box-sizing:border-box;margin:0;padding:0}
html,body{width:1200px;height:3906px;overflow:hidden}
body{font-family:"Poppins",sans-serif;color:var(--text);background:var(--white);position:relative}
.abs{position:absolute}
a{color:inherit;text-decoration:none}
.btn{position:absolute;display:flex;align-items:center;justify-content:center;border-radius:20px;font-size:10.5px;font-weight:500;letter-spacing:.3px}
.btn-green{background:var(--green);color:#fff}
.btn-outline{border:1.5px solid #cfd6de;color:var(--text);background:#fff}
.sec-title{position:absolute;left:0;width:1200px;text-align:center;font-size:29px;font-weight:500;color:var(--text)}
.sec-sub{position:absolute;left:0;width:1200px;text-align:center;font-size:12px;color:var(--muted)}
/* hero */
.hero-bg{left:0;top:0;width:1200px;height:820px;background:linear-gradient(135deg,#eaf7f1 0%,#f3f9fb 55%,#f5f8fc 100%)}
.brand{left:93px;top:44px;display:flex;align-items:center;gap:10px;font-size:25px;font-weight:600;color:var(--navy)}
.brand i{width:16px;height:16px;background:var(--green);border-radius:3px;display:block}
.nav{left:404px;top:34px;display:flex;gap:22px;font-size:10.5px;font-weight:500;color:#2b3140;align-items:center}
.nav-contact{left:910px;top:35px;font-size:10.5px;font-weight:500;color:#2b3140}
.nav-demo{left:978px;top:26px;width:130px;height:32px;background:var(--blue);color:#fff}
.badge{left:93px;top:244px;padding:5px 12px;border-radius:14px;background:#d8f0e5;color:var(--green-dark);font-size:11px;font-weight:500}
.hero-h{left:93px;top:283px;width:560px;font-size:37px;line-height:46px;font-weight:500}
.hero-p{left:93px;top:384px;width:470px;font-size:11.5px;line-height:20px;color:#4d5563}
/* dashboard */
.dash{left:664px;top:162px;width:536px;height:424px;background:#fff;border-radius:14px 0 0 14px;box-shadow:0 10px 40px rgba(30,50,80,.12);overflow:hidden;font-size:6.5px;color:#444}
.dash .side{position:absolute;left:10px;top:38px;width:78px;height:376px;border-right:1px solid var(--line)}
.dash .side div{padding:4px 6px;color:#555}
.dash .card{position:absolute;border:1px solid var(--line);border-radius:6px;background:#fff;padding:6px}
.dash .num{font-size:10px;font-weight:600;color:#222;margin-top:8px}
/* trusted */
.trust-band{left:0;top:695px;width:1200px;height:125px}
.trust-label{left:97px;top:726px;font-size:17px;font-weight:500}
.logo-name{position:absolute;top:738px;font-size:22px;font-weight:500;color:#a6abb3;display:flex;align-items:center;gap:8px}
.logo-name i{width:18px;height:18px;background:#c3c7cd;display:block;border-radius:3px}
/* features */
.feature{position:absolute;top:994px;width:248px;height:210px;border-radius:14px;padding:40px 0 0 41px}
.feature .ico{width:40px;height:40px;border-radius:8px;background:#fff;display:flex;align-items:center;justify-content:center}
.feature h3{font-size:13.5px;font-weight:600;margin-top:27px}
.feature p{font-size:10.5px;line-height:16px;color:var(--muted);margin-top:8px;width:175px}
/* how */
.step-label{position:absolute;font-size:13.5px;font-weight:600}
.step-text{position:absolute;font-size:10.5px;line-height:16px;color:var(--muted)}
/* results */
.results-bg{left:0;top:1808px;width:1200px;height:502px;background:#f4f6f8;border-radius:40px}
.quote{position:absolute;top:1995px;width:248px;height:160px;background:#fff;border-radius:12px;padding:30px 0 0 32px}
.quote .qm{font-size:30px;line-height:20px;color:var(--blue);font-weight:600;font-family:Georgia,serif}
.quote p{font-size:10.5px;line-height:16px;color:var(--muted);margin-top:10px;width:200px}
.quote .who{font-size:10.5px;color:#333;margin-top:5px}
.quote .stars{color:var(--star);font-size:12px;letter-spacing:1px;margin-top:3px}
/* insights */
.post{position:absolute;top:2500px;height:361px;border-radius:14px}
.post-img{position:absolute;border-radius:10px}
.post .read{position:absolute;font-size:11.5px;color:#444}
.post h4{position:absolute;font-size:16.5px;font-weight:500;line-height:23px}
/* pricing */
.plan{position:absolute;top:3045px;width:245px;height:161px;border:1.5px solid var(--line);border-radius:14px;text-align:center;background:#fff}
.plan h5{font-size:17px;font-weight:500;margin-top:40px}
.plan .price{font-size:25px;font-weight:500;margin-top:2px}
.plan p{font-size:11.5px;color:var(--muted);margin-top:4px;line-height:18px}
/* demo */
.demo-h{left:226px;top:3309px;font-size:27px;font-weight:500}
.demo-p{left:226px;top:3352px;width:330px;font-size:11.5px;line-height:21px;color:var(--muted)}
.demo-list{left:226px;top:3401px;font-size:11.5px;line-height:22px;color:var(--muted);list-style:none}
.footer-bg{left:0;top:3527px;width:1200px;height:379px;background:var(--mint2);border-radius:60px 60px 0 0}
.form{left:683px;top:3246px;width:297px;height:311px;background:#f3f5f7;border-radius:4px}
.field{position:absolute;left:17px;width:263px;height:29px;background:#fff;border:1px solid #dde2e8;border-radius:4px;font-size:10.5px;color:#8a919c;padding:7px 9px}
/* footer */
.f-col{position:absolute;top:3674px}
.f-col h6{font-size:14.5px;font-weight:500;margin-bottom:8px}
.f-col a{display:block;font-size:11.5px;color:var(--muted);line-height:22px}
.copyright{left:0;top:3876px;width:1200px;text-align:center;font-size:10.5px;color:var(--muted)}
</style>
</head>
<body>

<!-- HERO -->
<div class="abs hero-bg"></div>
<div class="abs brand"><i></i>PollMeridian</div>
<nav class="abs nav">
  <svg width="13" height="12" viewBox="0 0 13 12"><path d="M6.5 0 0 5.5h2V12h3.5V8h2v4H11V5.5h2z" fill="var(--green)"/></svg>
  <a>PRODUCT</a><a>SERVICES</a><a>RESOURCES</a><a>PRICING</a><a>ABOUT</a>
</nav>
<a class="abs nav-contact">CONTACT</a>
<a class="btn nav-demo">REQUEST A DEMO</a>

<div class="abs badge">CX Platform + Experts</div>
<h1 class="abs hero-h">Turn customer feedback into measurable loyalty.</h1>
<p class="abs hero-p">Real-time customer feedback, leadership-ready reporting, and expert CX guidance — all in one platform. Find churn risks early, close the loop with customers, and drive retention that shows up on the bottom line.</p>
<a class="btn btn-green" style="left:93px;top:458px;width:128px;height:32px">REQUEST A DEMO</a>
<a class="btn btn-outline" style="left:227px;top:458px;width:128px;height:32px">SEE PLATFORM</a>

<!-- Dashboard preview -->
<div class="abs dash" role="group" aria-label="Support dashboard preview">
  <svg class="abs" style="left:14px;top:15px" width="40" height="8"><circle cx="4" cy="4" r="3.5" fill="#14a878"/><circle cx="15" cy="4" r="3.5" fill="#1f56a8"/><circle cx="26" cy="4" r="3.5" fill="#dfe3e8"/></svg>
  <div class="abs" style="left:20px;top:45px;font-size:8px;font-weight:600;color:var(--navy)">PollMeridian</div>
  <div class="abs" style="left:106px;top:48px;color:#777">Support / <b style="color:#222">Support Overview</b></div>
  <div class="abs" style="left:486px;top:45px;background:#111;color:#fff;border-radius:8px;padding:2px 7px">+ Add New</div>
  <div class="side" style="top:70px">
    <div>Activity</div><div style="margin-top:12px">Dashboard</div><div>Clients</div><div>Orders</div><div>Billing</div><div>Reports</div><div>Utilities</div><div>Addons</div><div>Settings</div>
    <div style="background:#f1f3f6;border-radius:4px;font-weight:600">Support</div>
    <div style="margin-top:12px">Library Product</div><div>Invoices</div><div>Automation</div>
    <div style="position:absolute;top:318px;border:1px solid var(--line);border-radius:5px;width:62px">Need Help?</div>
  </div>
  <div class="card" style="left:110px;top:74px;width:104px;height:42px">All tickets<div class="num">2,300</div></div>
  <div class="card" style="left:219px;top:74px;width:104px;height:42px">Client replies<div class="num">112</div></div>
  <div class="card" style="left:328px;top:74px;width:104px;height:42px">Staff replies<div class="num">1,678</div></div>
  <div class="card" style="left:437px;top:74px;width:104px;height:42px">Tickets without reply<div class="num">1,678</div></div>
  <div class="card" style="left:110px;top:122px;width:272px;height:98px">Ticket reply time<div class="num" style="margin-top:2px">1,679</div>
    <svg class="abs" style="left:4px;top:30px" width="262" height="60" viewBox="0 0 262 60"><path d="M0 55 L30 45 L55 50 L75 25 L95 38 L115 44 L140 30 L165 20 L185 34 L210 26 L230 40 L262 44 L262 60 L0 60Z" fill="#e4f5ee"/><path d="M0 55 L30 45 L55 50 L75 25 L95 38 L115 44 L140 30 L165 20 L185 34 L210 26 L230 40 L262 44" fill="none" stroke="#14a878" stroke-width="1.5"/><rect x="140" y="2" width="48" height="14" rx="2" fill="#111"/><text x="146" y="12" font-size="5.5" fill="#fff">400 reply</text></svg>
  </div>
  <div class="card" style="left:388px;top:122px;width:153px;height:98px">Ticket priority
    <svg class="abs" style="left:36px;top:18px" width="80" height="46" viewBox="0 0 80 46"><path d="M8 40 A32 32 0 0 1 72 40" fill="none" stroke="#eef0f3" stroke-width="7"/><path d="M8 40 A32 32 0 0 1 24 13" fill="none" stroke="#1f56a8" stroke-width="7"/><path d="M26 12 A32 32 0 0 1 56 12" fill="none" stroke="#2aa3e8" stroke-width="7"/><path d="M58 14 A32 32 0 0 1 72 40" fill="none" stroke="#f3b73e" stroke-width="7"/><text x="40" y="38" font-size="8" font-weight="600" text-anchor="middle" fill="#222">1,500</text></svg>
    <div class="abs" style="left:20px;top:76px;font-size:5.5px;color:#777">● Email &nbsp; ● Live chat &nbsp; ● Messenger &nbsp; ● Contact form</div>
  </div>
  <div class="card" style="left:110px;top:226px;width:208px;height:166px">Average tickets created
    <div class="abs" style="left:8px;top:16px;font-size:5.5px">● Avg. Ticket Solved &nbsp;&nbsp; ● Avg. Ticket Created</div>
    <div class="abs" style="left:8px;top:26px;font-size:9px;font-weight:600;color:#222">1,654 &nbsp;&nbsp;&nbsp;&nbsp;&nbsp; 4,567</div>
    <svg class="abs" style="left:8px;top:50px" width="190" height="100" viewBox="0 0 190 100">
      <g fill="#c9ecdc"><rect x="14" y="10" width="14" height="82"/><rect x="40" y="30" width="14" height="62"/><rect x="66" y="45" width="14" height="47"/><rect x="92" y="20" width="14" height="72"/><rect x="118" y="30" width="14" height="62"/><rect x="144" y="38" width="14" height="54"/><rect x="170" y="25" width="14" height="67"/></g>
      <g fill="#14a878"><rect x="14" y="32" width="14" height="60"/><rect x="40" y="60" width="14" height="32"/><rect x="66" y="65" width="14" height="27"/><rect x="92" y="55" width="14" height="37"/><rect x="118" y="62" width="14" height="30"/><rect x="144" y="70" width="14" height="22"/><rect x="170" y="52" width="14" height="40"/></g>
    </svg>
  </div>
  <div class="card" style="left:324px;top:226px;width:217px;height:166px">Recent tickets
    <div style="margin-top:10px;line-height:24.5px;font-size:5.5px">
      <div>Feb 08 · Steps to reset the widget</div><div>Feb 11 · Export of survey results</div><div>Feb 09 · Theme colors not saving</div><div>Feb 09 · Alert rule sends twice</div><div>Feb 05 · NPS filter by region</div><div>Feb 05 · Invite more team seats</div>
    </div>
  </div>
</div>

<!-- TRUSTED BY -->
<svg class="abs trust-band" width="1200" height="125" viewBox="0 0 1200 125"><path d="M325 125 Q340 60 380 20 Q398 0 425 0 H1200 V125Z" fill="#fff"/></svg>
<div class="abs trust-label">Trusted by</div>
<div class="logo-name" style="left:437px"><i></i>Kestrel</div>
<div class="logo-name" style="left:625px">Brightpath</div>
<div class="logo-name" style="left:792px">Vantly</div>
<div class="logo-name" style="left:968px"><i></i>Cartwell</div>

<!-- PLATFORM & SERVICES -->
<h2 class="sec-title" style="top:900px">Platform &amp; Services that move the needle</h2>
<p class="sec-sub" style="top:947px">A unified CX platform with expert consulting to implement, interpret, and act on insights.</p>
<div class="feature" style="left:93px;background:var(--sky)"><div class="ico"><svg width="22" height="22" viewBox="0 0 22 22"><path d="M1 12h5l2-6 4 12 3-9 2 3h4" fill="none" stroke="#1f56a8" stroke-width="1.6"/></svg></div><h3>Real-time Feedback</h3><p>Collect feedback across channels with targeted surveys and microsurveys.</p></div>
<div class="feature" style="left:349px;background:#e6f5ee"><div class="ico"><svg width="22" height="22" viewBox="0 0 22 22"><path d="M11 2v18M2 11h18" stroke="#14a878" stroke-width="1.6"/></svg></div><h3>Churn-risk Alerts</h3><p>Automated alerts surface at-risk accounts for rapid intervention.</p></div>
<div class="feature" style="left:604px;background:var(--lav)"><div class="ico"><svg width="22" height="22" viewBox="0 0 22 22"><path d="M3 15a8 8 0 0 1 16 0" fill="none" stroke="#4654c8" stroke-width="2"/><circle cx="11" cy="13" r="3" fill="none" stroke="#4654c8" stroke-width="1.6"/></svg></div><h3>Leadership Reports</h3><p>Board-worthy dashboards and executive summaries for decision-makers.</p></div>
<div class="feature" style="left:859px;background:var(--gray)"><div class="ico"><svg width="22" height="22" viewBox="0 0 22 22"><path d="M3 7h5v8H3M13 7h5v8h-5" fill="none" stroke="#1c2333" stroke-width="1.6"/></svg></div><h3>CX Consulting</h3><p>Dedicated experts to help implement programs and coach teams.</p></div>

<!-- HOW IT WORKS -->
<h2 class="sec-title" style="top:1268px">How it works</h2>
<p class="sec-sub" style="top:1311px">Deploy targeted feedback, detect risk, and take action with expert support.</p>
<svg class="abs" style="left:459px;top:1345px" width="280" height="260" viewBox="0 0 280 260" role="img" aria-label="Three steps: deploy, detect, act">
  <g fill="none" stroke-width="3" stroke-linecap="round">
    <path d="M108 92 H172" stroke="#14a878"/><path d="M166 86 L173 92 L166 98" stroke="#14a878"/>
    <path d="M205 130 L160 190" stroke="#1f56a8"/><path d="M160 181 L159 192 L169 188" stroke="#1f56a8"/>
    <path d="M118 190 L76 130" stroke="#14a878"/><path d="M74 140 L75 129 L85 133" stroke="#14a878"/>
  </g>
  <rect x="20" y="52" width="82" height="82" rx="14" fill="none" stroke="#1f56a8" stroke-width="16"/>
  <rect x="178" y="52" width="82" height="82" rx="14" fill="none" stroke="#14a878" stroke-width="16"/>
  <rect x="99" y="170" width="82" height="82" rx="14" fill="none" stroke="#1f56a8" stroke-width="16"/>
  <g font-family="Poppins,sans-serif" font-size="22" font-weight="500" fill="#d7dde5" text-anchor="middle"><text x="61" y="101">01</text><text x="219" y="101">02</text><text x="140" y="219">03</text></g>
</svg>
<div class="step-label" style="left:392px;top:1440px">Deploy</div>
<div class="step-text" style="left:241px;top:1462px;width:200px;text-align:right">Omnichannel surveys, NPS, CSAT, and in-app microsurveys.</div>
<div class="step-label" style="left:757px;top:1440px">Detect</div>
<div class="step-text" style="left:757px;top:1462px;width:210px">AI-assisted segmentation and churn risk alerts for fast prioritization.</div>
<div class="step-label" style="left:0;width:1200px;text-align:center;top:1618px">Act</div>
<div class="step-text" style="left:500px;width:200px;text-align:center;top:1641px">Close the loop, coach reps, and measure impact on retention.</div>
<a class="btn btn-outline" style="left:535px;top:1699px;width:130px;height:33px">LEARN MORE</a>

<!-- RESULTS -->
<div class="abs results-bg"></div>
<h2 class="sec-title" style="top:1893px">Results that matter</h2>
<p class="sec-sub" style="top:1940px">Customers report improved retention and measurable ROI after deploying PollMeridian.</p>
<div class="quote" style="left:93px"><div class="qm">“</div><p>PollMeridian helped us reduce churn by 18% in 6 months.</p><div class="who">VP Customer Success • Crestline</div><div class="stars">★★★★★</div></div>
<div class="quote" style="left:349px"><div class="qm">“</div><p>Leadership finally has the metrics they trust.</p><div class="who">Head of CX • Harborview</div><div class="stars">★★★★★</div></div>
<div class="quote" style="left:604px"><div class="qm">“</div><p>Actionable alerts let us intervene before renewals.</p><div class="who">Customer Ops • Tidewell</div><div class="stars">★★★★★</div></div>
<div class="quote" style="left:859px"><div class="qm">“</div><p>The PollMeridian team helped us improve NPS scores across ...</p><div class="who">Customer Experience • Lumora</div><div class="stars">★★★★★</div></div>
<a class="btn btn-green" style="left:536px;top:2180px;width:128px;height:32px">SEE CASE STUDIES</a>

<!-- INSIGHTS -->
<h2 class="sec-title" style="top:2400px">Insights &amp; Resources</h2>
<p class="sec-sub" style="top:2447px">Stay up to date with the latest trends in customer experience, loyalty measurement, and retention strategies.</p>
<article class="post" style="left:93px;width:494px;background:linear-gradient(135deg,#e2e4e6,#c9cccf);overflow:hidden">
  <div class="post-img" role="img" aria-label="Hand holding a phone showing a star rating" style="left:0;top:0;width:494px;height:361px;background:linear-gradient(160deg,#e6e7e9 0%,#d3d5d8 60%,#c6c9cc 100%)"></div>
  <span class="read" style="left:59px;top:250px">4 min read</span>
  <h4 style="left:57px;top:274px;width:240px">Why customer feedback should be real-time</h4>
</article>
<article class="post" style="left:601px;width:246px;border:1.5px solid var(--line);background:#fff">
  <div class="post-img" role="img" aria-label="Man working at a laptop" style="left:6px;top:7px;width:232px;height:247px;background:linear-gradient(160deg,#cfdbe8,#8fa7c3)"></div>
  <span class="read" style="left:27px;top:274px">4 min read</span>
  <h4 style="left:27px;top:298px;width:200px">Turning alerts into actions: a playbook</h4>
</article>
<article class="post" style="left:860px;width:247px;border:1.5px solid var(--line);background:#fff">
  <div class="post-img" role="img" aria-label="Woman smiling at her desk" style="left:7px;top:7px;width:232px;height:247px;background:linear-gradient(160deg,#eee8e2,#c9b8a8)"></div>
  <span class="read" style="left:39px;top:274px">4 min read</span>
  <h4 style="left:38px;top:298px;width:190px">Measuring loyalty beyond NPS</h4>
</article>

<!-- PRICING -->
<h2 class="sec-title" style="top:2949px">Plans crafted for scaling teams</h2>
<p class="sec-sub" style="top:2996px">Transparent pricing or custom enterprise plans — request a demo and we'll recommend the right fit.</p>
<div class="plan" style="left:220px"><h5>Starter</h5><div class="price" style="color:var(--blue)">$99/mo</div><p>Basic surveys &amp; dashboards</p></div>
<div class="plan" style="left:478px"><h5>Pro</h5><div class="price" style="color:var(--green)">$499/mo</div><p>Advanced analytics &amp; alerts</p></div>
<div class="plan" style="left:736px"><h5>Enterprise</h5><p style="margin-top:10px">Custom – Dedicated CX<br>team &amp; SLA</p></div>

<!-- FOOTER BACKGROUND -->
<div class="abs footer-bg"></div>

<!-- REQUEST DEMO -->
<h2 class="abs demo-h">Request a demo</h2>
<p class="abs demo-p">Tell us a bit about your organization and goals — we'll tailor the demo to your priorities.</p>
<ul class="abs demo-list"><li>• Leadership-ready reports</li><li>• Churn-risk detection &amp; alerts</li><li>• Expert onboarding &amp; program consulting</li></ul>
<form class="abs form">
  <div class="field" style="top:26px">Full name</div>
  <div class="field" style="top:67px">Work email</div>
  <div class="field" style="top:107px">Company</div>
  <div class="field" style="top:147px;color:#333">I'm interested in...<svg class="abs" style="right:8px;top:11px" width="8" height="6"><path d="M1 1l3 3 3-3" fill="none" stroke="#333" stroke-width="1.4"/></svg></div>
  <div class="field" style="top:184px;height:67px">Short note (goals, timeline, team size)</div>
  <a class="btn btn-green" style="left:85px;top:261px;width:127px;height:30px">REQUEST DEMO</a>
</form>

<!-- FOOTER -->
<div class="abs brand" style="left:149px;top:3695px;font-size:28px"><i style="width:20px;height:20px"></i>PollMeridian</div>
<div class="f-col" style="left:484px"><h6>Product Links</h6><a>Platform</a><a>Services</a><a>Pricing</a></div>
<div class="f-col" style="left:674px"><h6>Company Links</h6><a>About</a><a>Resources</a><a>Contact</a></div>
<div class="f-col" style="left:878px"><h6>Newsletter</h6><a>Subscribe to our newsletter</a></div>
<div class="abs" style="left:877px;top:3723px;width:175px;height:27px;background:#fff;border-radius:14px;font-size:10px;color:#555;padding:6px 16px">Email Address
  <svg class="abs" style="right:12px;top:8px" width="12" height="11" viewBox="0 0 12 11"><path d="M0 5 12 0 9 11 6 7z" fill="var(--green)"/></svg></div>
<div class="abs" style="left:93px;top:3861px;width:1014px;height:1px;background:#cfe3da"></div>
<p class="abs copyright">© 2025 PollMeridian. All rights reserved. | Privacy | Terms</p>
<div class="abs" style="left:1124px;top:3842px;width:34px;height:34px;border-radius:50%;background:var(--blue);display:flex;align-items:center;justify-content:center">
  <svg width="12" height="8" viewBox="0 0 12 8"><path d="M1 7l5-5 5 5" fill="none" stroke="#fff" stroke-width="1.8"/></svg>
</div>

</body>
</html>
```